Lume Hart Co Need a custom graphic

I need to have the attached chart re-designed in a hand colored pencil format. The heading needs to be changed to "The most effective methods for hiring sales people". Do not include the background logo in the sample file.

Place the attached Lume Hart Co logo next to the most effective methods (91%)

```html
<!DOCTYPE html>
<html lang="en">
<head>
<meta charset="utf-8">
<title>Lume Hart Co – The Most Effective Methods for Hiring Sales People</title>
<link rel="stylesheet" href="https://fonts.googleapis.com/css2?family=Bebas+Neue&family=Montserrat:wght@500;700;800;900&display=swap">
<style>
  :root{
    --backdrop:#9c9c9c;
    --paper:#f7f9fc;
    --sky:#1d95d6;
    --navy:#1f2d6a;
    --grid:#bfe3f6;
    --panel:#b9e3f7;
    --ink:#1a1a2a;
    --shadow-band:#8d93ad;
  }
  html,body{margin:0;padding:0;width:1096px;height:1200px;overflow:hidden;background:var(--backdrop);}
  .poster{position:absolute;left:28px;top:277px;width:1040px;height:646px;box-shadow:0 10px 28px rgba(0,0,0,.35);background:var(--paper);}
  .poster svg{display:block;width:1040px;height:646px;}
  .title{font-family:"Bebas Neue",sans-serif;font-size:44px;fill:#fff;letter-spacing:.5px;}
  .brand{font-family:"Montserrat",sans-serif;font-weight:800;font-size:46px;fill:var(--navy);letter-spacing:1px;}
  .tagline{font-family:"Montserrat",sans-serif;font-weight:700;font-size:13px;fill:var(--navy);letter-spacing:1px;}
  .tick{font-family:"Montserrat",sans-serif;font-weight:800;font-size:13px;fill:var(--ink);}
  .axis-title{font-family:"Montserrat",sans-serif;font-weight:800;font-size:17px;fill:var(--sky);}
  .x-title{font-family:"Montserrat",sans-serif;font-weight:800;font-size:27px;fill:var(--navy);}
  .bar-label{font-family:"Montserrat",sans-serif;font-weight:900;font-size:17px;fill:var(--ink);}
  .bar-label tspan{font-size:9px;}
  .legend-pct{font-family:"Montserrat",sans-serif;font-weight:900;font-size:17px;fill:var(--ink);}
  .legend-pct tspan{font-size:9px;}
  .legend-text{font-family:"Montserrat",sans-serif;font-weight:800;font-size:11.5px;fill:var(--ink);}
  .grid line{stroke:var(--grid);stroke-width:1;}
  .bar-sky .face{fill:#fff;stroke:var(--sky);stroke-width:4;stroke-linejoin:round;}
  .bar-sky .side{fill:url(#hatch-sky);stroke:var(--sky);stroke-width:4;stroke-linejoin:round;}
  .bar-navy .face{fill:#fff;stroke:var(--navy);stroke-width:4;stroke-linejoin:round;}
  .bar-navy .side{fill:url(#hatch-navy);stroke:var(--navy);stroke-width:4;stroke-linejoin:round;}
</style>
</head>
<body>
<div class="poster">
<svg viewBox="0 0 1256 780" xmlns="http://www.w3.org/2000/svg">
  <defs>
    <pattern id="hatch-sky" width="5" height="5" patternUnits="userSpaceOnUse" patternTransform="rotate(45)">
      <rect width="5" height="5" fill="#fff"/><line x1="0" y1="0" x2="0" y2="5" stroke="var(--sky)" stroke-width="2"/>
    </pattern>
    <pattern id="hatch-navy" width="5" height="5" patternUnits="userSpaceOnUse" patternTransform="rotate(45)">
      <rect width="5" height="5" fill="#fff"/><line x1="0" y1="0" x2="0" y2="5" stroke="var(--navy)" stroke-width="2"/>
    </pattern>
  </defs>

  <rect class="paper" width="1256" height="780" fill="var(--paper)"/>

  <!-- header band -->
  <path class="header-shadow" d="M0 132 L640 140 Q690 142 705 110 L735 0 L725 0 L690 100 Q675 132 640 132 Z" fill="var(--shadow-band)"/>
  <path class="header-band" d="M0 0 H718 L680 100 Q668 128 630 130 H0 Z" fill="var(--sky)"/>
  <text class="title" x="112" y="68">THE MOST EFFECTIVE METHODS</text>
  <text class="title" x="112" y="108">FOR HIRING SALES PEOPLE</text>

  <!-- brand -->
  <rect class="brand-mark" x="1164" y="50" width="18" height="18" fill="var(--sky)"/>
  <text class="brand" x="780" y="98">LUME HART CO</text>
  <line x1="782" y1="115" x2="950" y2="115" stroke="var(--navy)" stroke-width="2"/>
  <text class="tagline" x="956" y="119">YOUR A.I. SALES RECRUITER</text>

  <!-- grid -->
  <g class="grid">
    <line x1="117" y1="161" x2="117" y2="686"/><line x1="195" y1="161" x2="195" y2="686"/>
    <line x1="273" y1="161" x2="273" y2="686"/><line x1="351" y1="161" x2="351" y2="686"/>
    <line x1="429" y1="161" x2="429" y2="686"/><line x1="507" y1="161" x2="507" y2="686"/>
    <line x1="585" y1="161" x2="585" y2="686"/><line x1="663" y1="161" x2="663" y2="686"/>
    <line x1="741" y1="161" x2="741" y2="686"/><line x1="819" y1="161" x2="819" y2="686"/>
    <line x1="897" y1="161" x2="897" y2="686"/><line x1="975" y1="161" x2="975" y2="686"/>
    <line x1="117" y1="161" x2="975" y2="161"/><line x1="117" y1="213" x2="975" y2="213"/>
    <line x1="117" y1="266" x2="975" y2="266"/><line x1="117" y1="318" x2="975" y2="318"/>
    <line x1="117" y1="370" x2="975" y2="370"/><line x1="117" y1="423" x2="975" y2="423"/>
    <line x1="117" y1="475" x2="975" y2="475"/><line x1="117" y1="527" x2="975" y2="527"/>
    <line x1="117" y1="580" x2="975" y2="580"/><line x1="117" y1="632" x2="975" y2="632"/>
    <line x1="117" y1="686" x2="975" y2="686"/>
  </g>

  <!-- y ticks -->
  <g class="ticks">
    <text class="tick" x="72" y="213">0.90</text><text class="tick" x="72" y="266">0.80</text>
    <text class="tick" x="72" y="318">0.70</text><text class="tick" x="72" y="370">0.60</text>
    <text class="tick" x="72" y="423">0.50</text><text class="tick" x="72" y="475">0.40</text>
    <text class="tick" x="72" y="527">0.30</text><text class="tick" x="72" y="580">0.20</text>
    <text class="tick" x="72" y="632">0.10</text><text class="tick" x="72" y="684">0.00</text>
  </g>

  <!-- axes -->
  <path class="axis" d="M55 202 H38 V308 M38 575 V725 H355" fill="none" stroke="var(--sky)" stroke-width="4"/>
  <text class="axis-title" transform="translate(44 562) rotate(-90)">PREDICTIVE VALIDITY</text>
  <text class="x-title" x="394" y="734">HIRING METODE</text>

  <!-- bars: x, top -->
  <g class="bar bar-sky"><path class="side" d="M182 614 L196 600 V670 L182 684 Z"/><path class="face" d="M132 614 L146 600 H196 L182 614 Z"/><rect class="face" x="132" y="614" width="50" height="70"/><text class="bar-label" x="138" y="658">13<tspan dy="-7">%</tspan></text></g>
  <g class="bar bar-navy"><path class="side" d="M258 590 L272 576 V670 L258 684 Z"/><path class="face" d="M208 590 L222 576 H272 L258 590 Z"/><rect class="face" x="208" y="590" width="50" height="94"/><text class="bar-label" x="215" y="632">18<tspan dy="-7">%</tspan></text></g>
  <g class="bar bar-sky"><path class="side" d="M336 575 L350 561 V670 L336 684 Z"/><path class="face" d="M286 575 L300 561 H350 L336 575 Z"/><rect class="face" x="286" y="575" width="50" height="109"/><text class="bar-label" x="291" y="620">20<tspan dy="-7">%</tspan></text></g>
  <g class="bar bar-navy"><path class="side" d="M412 575 L426 561 V670 L412 684 Z"/><path class="face" d="M362 575 L376 561 H426 L412 575 Z"/><rect class="face" x="362" y="575" width="50" height="109"/><text class="bar-label" x="367" y="620">20<tspan dy="-7">%</tspan></text></g>
  <g class="bar bar-sky"><path class="side" d="M490 559 L504 545 V670 L490 684 Z"/><path class="face" d="M440 559 L454 545 H504 L490 559 Z"/><rect class="face" x="440" y="559" width="50" height="125"/><text class="bar-label" x="446" y="602">23<tspan dy="-7">%</tspan></text></g>
  <g class="bar bar-navy"><path class="side" d="M566 559 L580 545 V670 L566 684 Z"/><path class="face" d="M516 559 L530 545 H580 L566 559 Z"/><rect class="face" x="516" y="559" width="50" height="125"/><text class="bar-label" x="522" y="602">23<tspan dy="-7">%</tspan></text></g>
  <g class="bar bar-sky"><path class="side" d="M642 511 L656 497 V670 L642 684 Z"/><path class="face" d="M592 511 L606 497 H656 L642 511 Z"/><rect class="face" x="592" y="511" width="50" height="173"/><text class="bar-label" x="598" y="546">33<tspan dy="-7">%</tspan></text></g>
  <g class="bar bar-navy"><path class="side" d="M718 417 L732 403 V670 L718 684 Z"/><path class="face" d="M668 417 L682 403 H732 L718 417 Z"/><rect class="face" x="668" y="417" width="50" height="267"/><text class="bar-label" x="676" y="456">51<tspan dy="-7">%</tspan></text></g>
  <g class="bar bar-sky"><path class="side" d="M796 391 L810 377 V670 L796 684 Z"/><path class="face" d="M746 391 L760 377 H810 L796 391 Z"/><rect class="face" x="746" y="391" width="50" height="293"/><text class="bar-label" x="751" y="428">57<tspan dy="-7">%</tspan></text></g>
  <g class="bar bar-navy"><path class="side" d="M872 313 L886 299 V670 L872 684 Z"/><path class="face" d="M822 313 L836 299 H886 L872 313 Z"/><rect class="face" x="822" y="313" width="50" height="371"/><text class="bar-label" x="834" y="350">71<tspan dy="-7">%</tspan></text></g>
  <g class="bar bar-sky"><path class="side" d="M948 210 L962 196 V670 L948 684 Z"/><path class="face" d="M898 210 L912 196 H962 L948 210 Z"/><rect class="face" x="898" y="210" width="50" height="474"/><text class="bar-label" x="906" y="249">91<tspan dy="-7">%</tspan></text></g>

  <!-- legend panel -->
  <rect class="legend-frame" x="993" y="157" width="240" height="540" rx="32" fill="none" stroke="var(--sky)" stroke-width="4"/>
  <rect class="legend-fill" x="1006" y="170" width="214" height="516" rx="22" fill="var(--panel)"/>
  <g class="legend">
    <text class="legend-pct" x="1022" y="210">91<tspan dy="-7">%</tspan></text>
    <text class="legend-text" x="1067" y="203">SALES-SPECIFIC</text><text class="legend-text" x="1067" y="217">MULTI-MEASUREMENT</text><text class="legend-text" x="1067" y="231">ASSESSMENT</text>
    <text class="legend-pct" x="1022" y="271">71<tspan dy="-7">%</tspan></text>
    <text class="legend-text" x="1067" y="264">MULTI-MEASUREMENT</text><text class="legend-text" x="1067" y="278">ASSESSMENT,</text>
    <text class="legend-pct" x="1022" y="318">57<tspan dy="-7">%</tspan></text>
    <text class="legend-text" x="1067" y="311">HIGHLY STRUCTURED</text><text class="legend-text" x="1067" y="325">INTERVIEW WITH</text><text class="legend-text" x="1067" y="339">SCORECARD</text>
    <text class="legend-pct" x="1022" y="379">51<tspan dy="-7">%</tspan></text>
    <text class="legend-text" x="1067" y="371">GENERAL MENTAL</text><text class="legend-text" x="1067" y="385">ABILITY</text>
    <text class="legend-pct" x="1022" y="421">33<tspan dy="-7">%</tspan></text>
    <text class="legend-text" x="1067" y="419">REFERENCE CHECK</text>
    <text class="legend-pct" x="1022" y="458">23<tspan dy="-7">%</tspan></text>
    <text class="legend-text" x="1067" y="450">BEHAVIOR/</text><text class="legend-text" x="1067" y="464">PERSONALITY TEST,</text>
    <text class="legend-pct" x="1022" y="497">23<tspan dy="-7">%</tspan></text>
    <text class="legend-text" x="1067" y="496">RESUME</text>
    <text class="legend-pct" x="1022" y="530">20<tspan dy="-7">%</tspan></text>
    <text class="legend-text" x="1067" y="529">SKILLS TEST</text>
    <text class="legend-pct" x="1022" y="565">20<tspan dy="-7">%</tspan></text>
    <text class="legend-text" x="1067" y="560">TRADITIONAL</text><text class="legend-text" x="1067" y="574">INTERVIEW</text>
    <text class="legend-pct" x="1022" y="607">18<tspan dy="-7">%</tspan></text>
    <text class="legend-text" x="1067" y="604">EMOTIONAL</text><text class="legend-text" x="1067" y="618">INTELLIGENCE</text>
    <text class="legend-pct" x="1022" y="651">13<tspan dy="-7">%</tspan></text>
    <text class="legend-text" x="1067" y="649">CULTURE TEST</text>
  </g>

  <!-- connector squares -->
  <line x1="1210" y1="635" x2="1115" y2="735" stroke="var(--navy)" stroke-width="7"/>
  <rect class="node" x="1182" y="607" width="62" height="60" rx="6" fill="var(--navy)"/>
  <rect class="node" x="1080" y="700" width="70" height="68" rx="6" fill="var(--navy)"/>

  <!-- bottom strip -->
  <rect class="footer-band" x="0" y="759" width="1040" height="21" fill="var(--sky)"/>
</svg>
</div>
</body>
</html>
```